Luxury Caviar Tin Label for High End Caviar Retailer

We are looking for a new caviar label design. We want something unique, preferably black and gold or dark blue and gold. We want a modern and luxurious feel. We have several types of caviar so we need to be able to change the name of the caviar when we print the labels. See inspiration attached. Logo is also attached. More about us: velmoronfare.com

Industry/Entity Type

fine foods industry, caviar

Font styles to use
Serif
Decorative

Requirements
Must have
• KT Velmoron Logo, space for caviar name
Nice to have
• black and gold, blue and gold

```html
<!DOCTYPE html>
<html lang="en">
<head>
<meta charset="utf-8">
<title>KT Velmoron Caviar Tin Label</title>
<link rel="stylesheet" href="https://fonts.googleapis.com/css2?family=Cinzel:wght@400;500&family=Marcellus&display=swap">
<style>
  :root {
    --page: #ffffff;
    --tin-black: #121212;
    --label-black: #1b1b1b;
    --rim-line: #2c2c2c;
    --gold: #d9b04a;
    --gold-light: #f3dc8c;
    --gold-deep: #9a7421;
  }
  html, body {
    margin: 0;
    width: 1200px;
    height: 960px;
    overflow: hidden;
    background: var(--page);
  }
  .label-canvas {
    display: block;
    width: 1200px;
    height: 960px;
  }
  .brand-name {
    font-family: "Marcellus", serif;
    font-size: 58px;
    letter-spacing: 1px;
    fill: var(--gold);
  }
  .product-type {
    font-family: "Marcellus", serif;
    font-size: 30px;
    letter-spacing: 1px;
    fill: var(--gold);
  }
  .variety-name {
    font-family: "Cinzel", serif;
    font-weight: 500;
    font-size: 38px;
    fill: var(--gold);
  }
  .rim-text {
    font-family: "Cinzel", serif;
    font-size: 16px;
    letter-spacing: 1.5px;
    fill: var(--gold);
  }
  .rim-text.small {
    font-size: 14px;
    letter-spacing: 0.5px;
  }
  .gold-arc {
    fill: none;
    stroke: url(#goldSheen);
    stroke-width: 7;
    stroke-linecap: butt;
  }
  .diamond-frame {
    fill: none;
    stroke: var(--gold);
    stroke-width: 2;
  }
</style>
</head>
<body>
<svg class="label-canvas" viewBox="0 0 1200 960" xmlns="http://www.w3.org/2000/svg">
  <defs>
    <linearGradient id="goldSheen" x1="0" y1="0" x2="1" y2="1">
      <stop offset="0" stop-color="var(--gold-deep)"/>
      <stop offset="0.45" stop-color="var(--gold-light)"/>
      <stop offset="1" stop-color="var(--gold-deep)"/>
    </linearGradient>
    <radialGradient id="crestTone" cx="0.5" cy="0.5" r="0.5">
      <stop offset="0" stop-color="#c99e3c"/>
      <stop offset="1" stop-color="#6e5420" stop-opacity="0.35"/>
    </radialGradient>
    <path id="path-ingredients" d="M307.3 311 A338 338 0 0 0 382.7 738.9"/>
    <path id="path-storage" d="M817.3 738.9 A338 338 0 0 0 892.7 311"/>
    <path id="path-weight" d="M457.2 786.3 A338 338 0 0 0 742.8 786.3"/>
  </defs>

  <!-- Label disc -->
  <circle class="label-disc" cx="600" cy="480" r="450" fill="var(--tin-black)"/>
  <circle class="label-rim" cx="600" cy="480" r="420" fill="none" stroke="var(--rim-line)" stroke-width="3"/>
  <circle class="label-field" cx="600" cy="480" r="405" fill="var(--label-black)"
          role="img" aria-label="Background pattern of fine concentric wave circles in dark grey"/>

  <!-- Gold arcs -->
  <path class="gold-arc" d="M329.7 290.6 A330 330 0 0 1 870.3 290.6"/>
  <path class="gold-arc" d="M410.7 750.3 A330 330 0 0 0 487.1 790.1"/>
  <path class="gold-arc" d="M712.9 790.1 A330 330 0 0 0 789.3 750.3"/>

  <!-- Rim text -->
  <text class="rim-text"><textPath href="#path-ingredients" startOffset="50%" text-anchor="middle">INGREDIENTS: LOREM IMPSUM</textPath></text>
  <text class="rim-text"><textPath href="#path-storage" startOffset="50%" text-anchor="middle">KEEP REFRIGERATED AT F28° - 38° /C</textPath></text>
  <text class="rim-text small"><textPath href="#path-weight" startOffset="50%" text-anchor="middle">NET WT. 114 G / 4 OZ</textPath></text>

  <!-- Crest area -->
  <ellipse class="crest-area" cx="600" cy="345" rx="165" ry="110" fill="url(#crestTone)"
           role="img" aria-label="Gold heraldic crest: shield with rampant lion framed by flourishes"/>

  <!-- Brand -->
  <text class="brand-name" x="600" y="512" text-anchor="middle">KT VELMORON</text>

  <!-- Product type badge -->
  <g class="product-badge">
    <polygon class="diamond-frame" points="600,548 690,612 600,676 510,612"/>
    <polygon points="506,612 514,606 522,612 514,618" fill="var(--gold)"/>
    <polygon points="678,612 686,606 694,612 686,618" fill="var(--gold)"/>
    <rect x="522" y="594" width="156" height="38" fill="var(--label-black)"/>
    <rect class="diamond-frame" x="522" y="594" width="156" height="38" stroke-width="1.2"/>
    <text class="product-type" x="600" y="624" text-anchor="middle">CAVIAR</text>
  </g>

  <!-- Variety name slot -->
  <text class="variety-name" x="600" y="740" text-anchor="middle">NAME</text>
</svg>
</body>
</html>
```